Coralvale Meat Traders Business Cards

We require business cards revamped with our logo. A few details we would like to use.

1. Round Edges
2. Our logo over the top of a wagyu cattle background photo on one side of the card

Other side of the card has the below details.

1. Person Name (First & Last)
2. Job Position
3. Mobile Number
4. Email Address
5. Website Address

Simple & Neat.

Target Market(s)

Sales

Industry/Entity Type

Agriculture

Contact Information for Business Card

CORALVALE MEAT TRADERS

Colors

Designer to choose colors to be used in the design.

Requirements
Must have
• Company Logo

```html
<!DOCTYPE html>
<html lang="en">
<head>
<meta charset="utf-8">
<title>Coralvale Meat Traders – Business Cards</title>
<link href="https://fonts.googleapis.com/css2?family=Montserrat:wght@400;500;600;700&display=swap" rel="stylesheet">
<style>
  :root{
    --backdrop:#e9e4de;
    --maroon:#4d0f24;
    --maroon-text:#7a1a2e;
    --paper:#ffffff;
    --ink:#2b2b2b;
    --muted:#555555;
    --shadow:rgba(40,20,10,.28);
  }
  *{margin:0;padding:0;box-sizing:border-box}
  html,body{width:1200px;height:676px;overflow:hidden}
  body{
    background:var(--backdrop);
    font-family:'Montserrat',sans-serif;
    position:relative;
  }
  .card{
    position:absolute;
    width:520px;height:298px;
    border-radius:16px;
    box-shadow:0 10px 26px var(--shadow);
    overflow:hidden;
  }
  .card--front{left:45px;top:189px;background:var(--maroon)}
  .card--back{left:635px;top:189px;background:var(--paper)}

  .front-brand{
    position:absolute;inset:0;
    display:flex;align-items:center;justify-content:center;gap:14px;
    color:var(--paper);
  }
  .brand-dot{width:16px;height:16px;border-radius:50%;background:currentColor;flex:none}
  .brand-name{
    font-weight:700;font-size:30px;line-height:1.05;letter-spacing:.5px;
    text-transform:uppercase;
  }

  .back-brand{
    position:absolute;left:34px;top:102px;
    display:flex;align-items:center;gap:9px;
    color:var(--maroon-text);
  }
  .back-brand .brand-dot{width:11px;height:11px}
  .back-brand .brand-name{font-size:17px}

  .address{
    position:absolute;left:40px;top:196px;
    font-size:10.5px;color:var(--ink);
  }
  .divider{
    position:absolute;left:254px;top:86px;width:1.5px;height:92px;
    background:var(--maroon-text);
  }
  .contact{position:absolute;left:268px;top:86px}
  .person-name{font-weight:700;font-size:18px;color:var(--maroon-text)}
  .person-role{font-size:11px;color:var(--muted);margin:2px 0 10px}
  .contact-list{list-style:none}
  .contact-item{
    display:flex;align-items:center;gap:8px;
    font-size:11px;color:var(--ink);margin-bottom:7px;
  }
  .contact-item svg{width:10px;height:10px;fill:var(--maroon-text);flex:none}
</style>
</head>
<body>
  <section class="card card--front" aria-label="Business card front">
    <div class="front-brand">
      <span class="brand-dot"></span>
      <span class="brand-name">Coralvale<br>Meat Traders</span>
    </div>
  </section>

  <section class="card card--back" aria-label="Business card back">
    <div class="back-brand">
      <span class="brand-dot"></span>
      <span class="brand-name">Coralvale<br>Meat Traders</span>
    </div>
    <p class="address">42 Ridgeline Road Fernhill, QLD 4870</p>
    <div class="divider"></div>
    <div class="contact">
      <h1 class="person-name">Dana Whitfield</h1>
      <p class="person-role">Managing Director</p>
      <ul class="contact-list">
        <li class="contact-item">
          <svg viewBox="0 0 10 10"><path d="M2 0.5 L3.6 2.6 L2.7 3.6 Q3.8 5.9 6.4 7.3 L7.4 6.4 L9.5 8 L8.4 9.5 Q3.5 9 0.5 1.6 Z"/></svg>
          555.204.7731
        </li>
        <li class="contact-item">
          <svg viewBox="0 0 10 10"><path d="M0.5 2 H9.5 V8.5 H0.5 Z M1.2 2.6 L5 5.6 L8.8 2.6 V3.4 L5 6.4 L1.2 3.4 Z" fill-rule="evenodd"/></svg>
          hello@coralvalemeat.com
        </li>
        <li class="contact-item">
          <svg viewBox="0 0 10 10"><circle cx="5" cy="5" r="4.5"/><path d="M0.8 5 H9.2 M5 0.6 Q2.4 5 5 9.4 M5 0.6 Q7.6 5 5 9.4" stroke="#fff" stroke-width=".8" fill="none"/></svg>
          www.coralvalemeat.com
        </li>
      </ul>
    </div>
  </section>
</body>
</html>
```